Company or website name
- LORAVEX
- Links to the website
- WWW.LORAVEX.NET
- Describe your company and organization and target audience
- check the website: www.loravex.net
- The design should have the following
- A clean visual is expected. The documents should include the complete address, emails, phone, name and position.
- Other Facts

```html
<!DOCTYPE html>
<html lang="en">
<head>
<meta charset="utf-8">
<title>LORAVEX Business Card</title>
<link href="https://fonts.googleapis.com/css2?family=Montserrat:wght@400;500&family=Open+Sans:wght@400;600&display=swap" rel="stylesheet">
<style>
  :root {
    --navy: #0f3658;
    --cyan: #5bbcd0;
    --paper: #ffffff;
    --paper-shade: #f1f1f1;
    --backdrop: #e9e6e3;
    --ink-light: #ffffff;
  }
  * { box-sizing: border-box; margin: 0; padding: 0; }
  html, body {
    width: 1200px; height: 944px; overflow: hidden;
    background: var(--backdrop);
  }
  .canvas {
    position: relative; width: 1200px; height: 944px;
    display: flex; align-items: center; justify-content: center; gap: 40px;
  }
  .card {
    position: relative; width: 540px; height: 309px; overflow: hidden;
    box-shadow: 0 6px 18px rgba(0,0,0,0.15);
  }
  /* Front side */
  .card-front {
    background: var(--navy);
    font-family: "Montserrat", sans-serif;
  }
  .brand-line {
    position: absolute; left: 0; right: 0; top: 128px;
    text-align: center; font-size: 21px; font-weight: 500;
    letter-spacing: 0.5px; color: var(--ink-light);
  }
  .brand-line .descriptor { color: var(--cyan); margin-left: 6px; }
  .front-url {
    position: absolute; left: 0; right: 0; bottom: 36px;
    text-align: center; font-size: 11px; letter-spacing: 3px;
    color: var(--ink-light); font-family: "Open Sans", sans-serif;
  }
  /* Back side */
  .card-back {
    background: linear-gradient(135deg, var(--paper), var(--paper-shade));
    font-family: "Open Sans", sans-serif;
  }
  .wave { position: absolute; inset: 0; }
  .company-name {
    position: absolute; left: 38px; top: 112px;
    font-family: "Montserrat", sans-serif; font-weight: 400;
    font-size: 46px; letter-spacing: 1px; color: var(--navy);
  }
  .person { position: absolute; left: 60px; top: 188px; color: var(--navy); }
  .person-name { font-size: 18px; font-weight: 600; line-height: 1.1; }
  .person-role { font-size: 11px; }
  .contact {
    position: absolute; right: 18px; top: 128px;
    list-style: none; text-align: right; color: var(--ink-light);
    font-size: 11px; line-height: 1.35;
  }
  .contact li { display: flex; justify-content: flex-end; align-items: center; gap: 6px; }
  .contact .address { margin-bottom: 10px; display: block; padding-right: 17px; }
  .contact svg { width: 11px; height: 11px; flex: none; }
</style>
</head>
<body>
<main class="canvas">
  <section class="card card-front" aria-label="Business card front">
    <p class="brand-line"><span class="brand-name">LORAVEX</span><span class="descriptor">DRILLING SUPPLIES</span></p>
    <p class="front-url">www.loravex.net</p>
  </section>

  <section class="card card-back" aria-label="Business card back">
    <svg class="wave" viewBox="0 0 540 309" preserveAspectRatio="none" aria-hidden="true">
      <path fill="var(--cyan)" d="M100 300 C270 292 300 222 334 142 C370 64 436 22 540 8 L540 22 C452 34 404 72 370 150 C332 236 290 296 100 300 Z"/>
      <path fill="var(--navy)" d="M150 309 C290 300 318 238 350 164 C384 88 440 46 540 36 L540 309 Z"/>
      <path fill="var(--navy)" d="M128 306 C270 296 300 236 332 164 C312 240 284 298 150 309 Z"/>
    </svg>
    <h1 class="company-name">LORAVEX</h1>
    <div class="person">
      <p class="person-name">Miles Harrowden</p>
      <p class="person-role">President</p>
    </div>
    <ul class="contact">
      <li class="address">Villa Sol, Altos del Mar<br>Ciudad Brisa</li>
      <li>+507 555-0142
        <svg viewBox="0 0 12 12"><path fill="none" stroke="currentColor" stroke-width="1.4" d="M2.5 1.5 L4.5 1.5 L5 4 L3.8 5 Q5 7.5 7 8.2 L8 7 L10.5 7.5 L10.5 9.5 Q6 11 2 6 Q1.5 3.5 2.5 1.5 Z"/></svg></li>
      <li>+507 5550-0187
        <svg viewBox="0 0 12 12"><rect x="3" y="1" width="6" height="10" rx="1" fill="none" stroke="currentColor" stroke-width="1.2"/></svg></li>
      <li>sales@loravex.net
        <svg viewBox="0 0 12 12"><rect x="1" y="2.5" width="10" height="7" fill="currentColor"/><path d="M1 2.5 L6 6.5 L11 2.5" fill="none" stroke="var(--navy)" stroke-width="1"/></svg></li>
      <li>www.loravex.net
        <svg viewBox="0 0 12 12"><circle cx="6" cy="6" r="5" fill="currentColor"/></svg></li>
    </ul>
  </section>
</main>
</body>
</html>
```